MCP phase 1 web design

Meridale Capital Partners Ltd (MCP) is a challenger business to the traditional leasing market. We look for solutions to complex problems involving the funding of capital equipment within an office environment and then build documentation around the solution. We recently created a brief for a logo and successfully completed that assignment. We now need to create our first web site which is simply intended to be informative. To help interested designers we have attached a detailed brief that is broken into three sections. The first explains how we see the site developing over time from something quite straightforward initially to a full transaction capability. Whoever wins this competition will be expected to work with us into the future to help develop the site. Section 2 gives you a view about our likes and dislikes by reviewing some existing sites. Section 3 gives you the structure and content of the site based upon our likes and dislikes. We are by no means committed to the structure and if you believe it can be presented in a better way then please use your design. The text is fixed as content. The images to appear can be anything from photographs to line drawings again entirely at the designers whim. Currently we have a home page plus 5 subsidiary pages. A few things to help you:
1. The logo is fixed and should be amongst the downloads.
2. The colours we have are corporate and should be used.
3. The typeface we use within the business is "Verdana"
Good luck.

```html
<!DOCTYPE html>
<html lang="en">
<head>
<meta charset="utf-8">
<title>Public Sector Solutions – Meridale Capital Partners Ltd</title>
<link rel="stylesheet" href="https://fonts.googleapis.com/css2?family=Noto+Sans:wght@400&display=swap">
<style>
:root{
  --brand-blue:#1a6fb5;
  --text-grey:#555;
  --menu-grey:#5c5c5c;
  --bg-light:#f2f2f2;
  --bg-dark:#dcdcdc;
  --white:#fff;
}
*{margin:0;padding:0;box-sizing:border-box}
html,body{width:1200px;height:1000px;overflow:hidden;background:var(--white);font-family:'Noto Sans',sans-serif}
.page-bg{position:absolute;left:0;top:0;width:1200px;height:897px;
  background:radial-gradient(ellipse 700px 420px at 600px 420px,var(--bg-light),var(--bg-dark))}
.site-header{position:absolute;left:0;top:0;width:1200px;height:68px;background:var(--white);
  border-top:5px solid var(--brand-blue);box-shadow:0 2px 3px rgba(0,0,0,.45);z-index:2}
.brand{position:absolute;left:112px;top:14px;display:flex;align-items:center;gap:10px;
  color:var(--brand-blue);font-size:21px;letter-spacing:.3px}
.brand-mark{width:34px;height:34px;background:var(--brand-blue)}
.main-nav{position:absolute;top:22px;left:0;font-size:17px;color:var(--text-grey)}
.main-nav span{position:absolute;white-space:nowrap}
.main-nav .active{color:var(--brand-blue)}
.content-panel{position:absolute;left:100px;top:82px;width:1000px;height:574px;background:var(--white);border-radius:8px;z-index:1}
.page-title{position:absolute;left:9px;top:20px;font-size:31px;font-weight:400;color:var(--brand-blue)}
.hero-photo{position:absolute;left:1px;top:68px;width:571px;height:341px;
  background:linear-gradient(100deg,#bdbdbd 0%,#d8d8d8 40%,#9a9a9a 70%,#222 100%)}
.intro-box{position:absolute;left:572px;top:68px;width:429px;height:341px;
  background:radial-gradient(ellipse 260px 200px at 55% 35%,#2f95e8,#1a6fb5);color:var(--white)}
.intro-text{position:absolute;left:12px;top:20px;width:380px;font-size:14.6px;line-height:17.3px}
.intro-text p+p{margin-top:17px}
.scrollbar{position:absolute;left:405px;top:7px;width:12px;height:329px;background:#3d9eef;border-radius:3px}
.scrollbar .thumb{position:absolute;left:1px;top:12px;width:10px;height:20px;background:#a9d3f7;border-radius:5px}
.dropdown{position:absolute;left:754px;top:69px;width:249px;height:111px;background:var(--menu-grey);
  border-radius:6px;box-shadow:2px 2px 4px rgba(0,0,0,.4);z-index:3;color:var(--white);font-size:16px}
.dropdown::before{content:"";position:absolute;left:107px;top:-12px;border:7px solid transparent;border-bottom:12px solid var(--menu-grey);border-top:0}
.dropdown li{list-style:none;position:absolute;left:8px;width:233px;height:25px;padding-left:4px;line-height:25px}
.dropdown li.current{background:var(--brand-blue)}
</style>
</head>
<body>
<div class="page-bg"></div>
<header class="site-header">
  <div class="brand"><span class="brand-mark"></span><span>Meridale Capital Partners Ltd</span></div>
  <nav class="main-nav">
    <span style="left:497px">HOME</span>
    <span style="left:602px">WHY ALTERNATIVE?</span>
    <span class="active" style="left:822px">SOLUTIONS ▾</span>
    <span style="left:1005px">CONTACT</span>
  </nav>
</header>
<ul class="dropdown">
  <li style="top:16px">Managed Services</li>
  <li class="current" style="top:45px">Public Sector</li>
  <li style="top:74px">Education</li>
</ul>
<main class="content-panel">
  <h1 class="page-title">Public Sector Solutions</h1>
  <div class="hero-photo" role="img" aria-label="Black and white photograph of a row of classical stone columns"></div>
  <div class="intro-box">
    <div class="intro-text">
      <p>Most public sector bodies increasingly require contract flexibility. In particular, some large tender frameworks contain clauses that make funding off balance sheet extremely difficult. Two examples are the ability to assign and walk-away clauses, which require the VAR to potentially take back hardware and discontin-ue technology solutions in case of closure or downsizing of a department with the total loss falling on the VAR.</p>
      <p>Such clauses made it difficult for many VARs to finance large tender frameworks, leaving only the largest VARs and some manufactur-ers to compete in this important market. MCP developed a solution that mitigates these risks which is incorporated into our financing tool.</p>
    </div>
    <div class="scrollbar"><div class="thumb"></div></div>
  </div>
</main>
</body>
</html>
```